4 x Designs Required

Hi There,
I require 4 x different designs to be made for 4 new brands of mine however they can be quite interchangeable. HR Plinkr and Marketing Plinkr can be similar just with a difference in colour. The same goes for the Bulletin brands. This means there are ultimately two designs that need perfecting.

There must be a click here CTA on the banner somewhere. :-)

I require the banners in 728x90 format and 960x90 please.

Please use strap lines on the banners such as:
Essential Whitepapers for HR Professionals
Essential Whitepapers for Marketing Professionals
Your No.1 Whitepaper Resource

The brand names:
HR Plinkr
Marketing Plinkr
HR Dispatchly
Marketing Dispatchly

Examples attached.

```html
<!DOCTYPE html>
<html lang="en">
<head>
<meta charset="utf-8">
<title>Banner Set – HR Plinkr &amp; HR Dispatchly</title>
<link rel="stylesheet" href="https://fonts.googleapis.com/css2?family=Montserrat:wght@400;800;900&family=Arimo:wght@400&display=swap">
<style>
  :root {
    --stage: #b3b3b3;
    --brand-blue: #0033a0;
    --brand-orange: #ff6600;
    --orange-light: #ff9a4d;
    --panel-light: #f1f1f1;
    --panel-lighter: #fafafa;
    --white: #ffffff;
    --label: #111111;
  }
  * { box-sizing: border-box; margin: 0; padding: 0; }
  html, body { width: 1200px; height: 1200px; overflow: hidden; }
  body {
    position: relative;
    background: var(--stage);
    font-family: "Montserrat", sans-serif;
  }
  .banner {
    position: absolute;
    height: 94px;
    overflow: hidden;
    background: linear-gradient(120deg, var(--panel-light) 0%, var(--panel-lighter) 35%, var(--panel-light) 60%, var(--panel-lighter) 100%);
  }
  .banner--wide { left: 99px; width: 1002px; }
  .banner--leader { left: 220px; width: 760px; }
  .banner__shapes { position: absolute; inset: 0; }
  .banner__text { position: absolute; white-space: nowrap; }

  .brand-name {
    position: absolute;
    top: 50%;
    transform: translateY(-50%);
    font-weight: 900;
    color: var(--brand-orange);
    white-space: nowrap;
  }
  .size-label {
    position: absolute;
    left: 0; width: 1200px;
    text-align: center;
    font-family: "Arimo", sans-serif;
    font-size: 32px;
    color: var(--label);
  }

  /* Plinkr design */
  .pill-headline {
    font-weight: 900;
    color: var(--white);
    top: 50%;
    transform: translateY(-50%);
    letter-spacing: -0.5px;
  }
  .pill-strap {
    font-weight: 900;
    color: var(--white);
    line-height: 1.08;
    top: 50%;
    transform: translateY(-50%);
  }
  .cta {
    position: absolute;
    display: flex;
    align-items: center;
    justify-content: center;
    border-radius: 999px;
    font-weight: 800;
    white-space: nowrap;
  }
  .cta--light {
    background: linear-gradient(180deg, #ffffff 0%, #e9e9e9 100%);
    color: var(--brand-blue);
  }
  .cta--dark {
    background: linear-gradient(180deg, #1f52c4 0%, var(--brand-blue) 60%);
    color: var(--white);
    border: 2px solid #dfe6f5;
  }

  /* Dispatchly design */
  .band-title {
    font-weight: 900;
    color: var(--white);
    transform: translateX(-50%);
    text-align: center;
  }
  .band-sub {
    font-weight: 400;
    color: var(--white);
    transform: translateX(-50%);
    text-align: center;
  }
</style>
</head>
<body>

  <!-- Plinkr 960x90 -->
  <div class="banner banner--wide" style="top:224px">
    <svg class="banner__shapes" width="1002" height="94" viewBox="0 0 1002 94">
      <defs>
        <linearGradient id="pillGloss" x1="0" y1="0" x2="0" y2="1">
          <stop offset="0" stop-color="#ff9a4d"/>
          <stop offset="0.45" stop-color="#ff6600"/>
          <stop offset="1" stop-color="#ff6600"/>
        </linearGradient>
      </defs>
      <rect x="708" y="0" width="294" height="94" fill="#0033a0"/>
      <rect x="254" y="0" width="493" height="94" rx="47" fill="url(#pillGloss)"/>
    </svg>
    <div class="brand-name" style="left:30px;font-size:31px">HR Plinkr</div>
    <div class="banner__text pill-headline" style="left:295px;font-size:40px">Your No.1</div>
    <div class="banner__text pill-strap" style="left:524px;font-size:23px">WHITEPAPER<br>RESOURCE</div>
    <div class="cta cta--light" style="left:794px;top:32px;width:161px;height:31px;font-size:20px">CLICK HERE</div>
  </div>
  <div class="size-label" style="top:340px">960x90</div>

  <!-- Plinkr 728x90 -->
  <div class="banner banner--leader" style="top:396px">
    <svg class="banner__shapes" width="760" height="94" viewBox="0 0 760 94">
      <defs>
        <linearGradient id="pillGloss2" x1="0" y1="0" x2="0" y2="1">
          <stop offset="0" stop-color="#ff9a4d"/>
          <stop offset="0.45" stop-color="#ff6600"/>
          <stop offset="1" stop-color="#ff6600"/>
        </linearGradient>
      </defs>
      <rect x="525" y="0" width="235" height="94" fill="#0033a0"/>
      <rect x="193" y="0" width="374" height="94" rx="47" fill="url(#pillGloss2)"/>
    </svg>
    <div class="brand-name" style="left:18px;font-size:26px">HR Plinkr</div>
    <div class="banner__text pill-headline" style="left:225px;font-size:32px">Your No.1</div>
    <div class="banner__text pill-strap" style="left:397px;font-size:19px">WHITEPAPER<br>RESOURCE</div>
    <div class="cta cta--light" style="left:598px;top:32px;width:131px;height:30px;font-size:17px">CLICK HERE</div>
  </div>
  <div class="size-label" style="top:510px">728x90</div>

  <!-- Dispatchly 960x90 -->
  <div class="banner banner--wide" style="top:664px">
    <svg class="banner__shapes" width="1002" height="94" viewBox="0 0 1002 94">
      <polygon points="299,94 330,32 361,94" fill="#ff6600"/>
      <polygon points="707,0 749,0 724,48" fill="#ff6600"/>
      <polygon points="299,0 707,0 749,94 341,94" fill="#0033a0"/>
    </svg>
    <div class="brand-name" style="left:30px;font-size:36px">HR Dispatchly</div>
    <div class="banner__text band-title" style="left:523px;top:26px;font-size:23px">ESSENTIAL WHITEPAPERS</div>
    <div class="banner__text band-sub" style="left:523px;top:55px;font-size:15px">FOR MARKETING PROFESSIONALS</div>
    <div class="cta cta--dark" style="left:794px;top:29px;width:150px;height:34px;font-size:19px">CLICK HERE</div>
  </div>
  <div class="size-label" style="top:777px">960x90</div>

  <!-- Dispatchly 728x90 -->
  <div class="banner banner--leader" style="top:835px">
    <svg class="banner__shapes" width="760" height="94" viewBox="0 0 760 94">
      <polygon points="227,94 255,38 283,94" fill="#ff6600"/>
      <polygon points="535,0 577,0 553,45" fill="#ff6600"/>
      <polygon points="227,0 535,0 577,94 269,94" fill="#0033a0"/>
    </svg>
    <div class="brand-name" style="left:18px;font-size:27px">HR Dispatchly</div>
    <div class="banner__text band-title" style="left:402px;top:31px;font-size:18px">ESSENTIAL WHITEPAPERS</div>
    <div class="banner__text band-sub" style="left:402px;top:54px;font-size:12px">FOR MARKETING PROFESSIONALS</div>
    <div class="cta cta--dark" style="left:598px;top:32px;width:131px;height:30px;font-size:17px">CLICK HERE</div>
  </div>
  <div class="size-label" style="top:945px">728x90</div>

</body>
</html>
```